mno school poster design and change logo name

We already have a logo which only needs to be slightly modified with "school".
We also have two advertising faces, a girl and a boy, which should be on our poster.
Important key data:

bilingual D/E small classes
daycare
private kindergarten
private school from 2024

Poster size: 268,5 x 128 cm
We need logo sizes in different sizes
also for T-shirts.
Attached also a old poster

Target Market(s)

new clients

Colors
0094D4
00A9DD
6FCCEA
C7EBF8
E9F6FB
59FF00
82FF00
B8FF75
E3FFCB
F4FFEA
FFC000
F8CF3A
FAE287
FDF2CF
FEFAEE
F0912C
F2A743
F7CA91
FBE8D2
FDF5EE

```html
<!DOCTYPE html>
<html lang="en">
<head>
<meta charset="utf-8">
<title>mno Schools – Banner</title>
<link href="https://fonts.googleapis.com/css2?family=Nunito:wght@800;900&family=Comic+Neue:wght@700&family=Arimo:wght@700&display=swap" rel="stylesheet">
<style>
  :root {
    --orange: #F5A51E;
    --orange-deep: #F08A1E;
    --orange-soft: #F7CA91;
    --red: #E8432A;
    --blue: #17739F;
    --blue-light: #6FCCEA;
    --white: #FFFFFF;
    --paper: #F7F7F7;
    --ink: #111111;
    --stage: #E4E4E4;
  }
  html, body {
    margin: 0;
    padding: 0;
    width: 1056px;
    height: 1200px;
    overflow: hidden;
    background: var(--stage);
  }
  .banner-frame {
    position: absolute;
    left: 28px;
    top: 361px;
    width: 1000px;
    height: 478px;
    box-shadow: 0 6px 18px rgba(0,0,0,0.35);
  }
  .banner {
    position: absolute;
    left: 0;
    top: 0;
    width: 1620px;
    height: 775px;
    transform: scale(0.6173);
    transform-origin: 0 0;
    background: var(--paper);
    overflow: hidden;
    font-family: "Nunito", sans-serif;
  }
  .banner > * { position: absolute; }
  .backdrop, .bands { left: 0; top: 0; width: 1620px; height: 775px; }

  .photo-boy {
    left: 10px; top: 270px; width: 545px; height: 505px;
    border-radius: 46% 40% 0 0;
    background: radial-gradient(ellipse at 50% 30%, #E2B48F 0%, #C98E68 35%, #3FB1DF 70%, #2EA3D6 100%);
  }
  .photo-girl {
    left: 1000px; top: 350px; width: 590px; height: 425px;
    border-radius: 48% 48% 0 0;
    background: radial-gradient(ellipse at 50% 35%, #F1CDB3 0%, #D9A27E 30%, #A0704E 55%, #F2F2F2 85%);
  }
  .illustration-plane {
    left: 40px; top: 45px; width: 250px; height: 110px;
    border-radius: 20px;
    background: linear-gradient(90deg, #D9463A, #3E6FC4 50%, rgba(255,255,255,0));
    opacity: 0.8;
  }
  .illustration-pencils-top {
    left: 420px; top: 0; width: 300px; height: 55px;
    background: linear-gradient(90deg, #4FB3E6, #E43A8F 60%, #F08A1E);
    opacity: 0.75;
  }
  .illustration-pencils-bottom {
    left: 0; top: 590px; width: 130px; height: 185px;
    background: linear-gradient(90deg, #3A9B45, #E4382F 40%, #F3B12A 70%, rgba(255,255,255,0));
    opacity: 0.7;
  }

  .brand {
    left: 270px; top: 160px; width: 400px;
    text-align: center;
  }
  .brand-name {
    font-family: "Comic Neue", cursive;
    font-weight: 700;
    font-size: 62px;
    line-height: 1;
    color: var(--orange);
    white-space: nowrap;
    display: flex;
    align-items: center;
    justify-content: center;
    gap: 12px;
  }
  .brand-dot {
    width: 22px; height: 22px; border-radius: 50%;
    background: var(--orange);
  }
  .brand-tagline {
    margin-top: 6px;
    font-family: "Comic Neue", cursive;
    font-weight: 700;
    font-size: 20px;
    line-height: 1.1;
    color: var(--orange);
    white-space: nowrap;
  }

  .headline {
    left: 770px; top: 55px;
    margin: 0;
    font-weight: 900;
    font-size: 118px;
    line-height: 1;
    color: var(--blue);
    white-space: nowrap;
  }
  .subheadline {
    right: 125px; top: 172px;
    margin: 0;
    font-weight: 800;
    font-size: 82px;
    line-height: 1;
    color: var(--blue);
    white-space: nowrap;
  }

  .offer {
    font-family: "Comic Neue", cursive;
    font-weight: 700;
    margin: 0;
    line-height: 1;
    white-space: nowrap;
  }
  .offer-daycare {
    left: 690px; top: 285px;
    font-size: 112px;
    color: var(--white);
  }
  .offer-kindergarten {
    left: 690px; top: 440px; width: 370px;
    text-align: center;
    font-size: 66px;
  }
  .offer-kindergarten .accent { color: var(--blue); display: block; }
  .offer-kindergarten .plain { color: var(--white); display: block; }
  .offer-school {
    left: 440px; top: 612px;
    font-size: 58px;
    color: var(--white);
  }
  .offer-school .year { font-size: 66px; }

  .contact {
    left: 345px; top: 692px; width: 740px;
    text-align: center;
    font-family: "Arimo", sans-serif;
    font-weight: 700;
    color: var(--ink);
    white-space: nowrap;
  }
  .contact-address { font-size: 26px; line-height: 1.1; margin: 0; }
  .contact-line { font-size: 31px; line-height: 1.1; margin: 6px 0 0; }
</style>
</head>
<body>
  <div class="banner-frame">
    <div class="banner">
      <svg class="backdrop" viewBox="0 0 1620 775" aria-hidden="true">
        <path d="M0 0 H120 Q110 70 30 90 Q10 100 0 110 Z" fill="#F8CF3A" opacity="0.8"/>
        <path d="M0 0 H60 Q50 35 0 40 Z" fill="#F0912C"/>
        <path d="M725 0 H1620 V150 Q1560 450 1540 775 H400 C450 600 700 300 725 0 Z" fill="var(--orange)"/>
        <path d="M1400 0 H1620 V120 Q1520 110 1440 70 Q1400 40 1400 0 Z" fill="#F0912C" opacity="0.55"/>
        <path d="M1565 0 H1620 V55 Q1580 40 1565 0 Z" fill="#EE6A1C"/>
        <circle cx="760" cy="190" r="20" fill="var(--blue-light)"/>
        <circle cx="720" cy="170" r="7" fill="var(--blue-light)"/>
      </svg>

      <div class="illustration-plane" role="img" aria-label="Toy airplane illustration"></div>
      <div class="illustration-pencils-top" role="img" aria-label="Coloured pencils illustration"></div>
      <div class="illustration-pencils-bottom" role="img" aria-label="Coloured pencils and notebook illustration"></div>

      <div class="photo-boy" role="img" aria-label="Photo of a laughing boy showing paint-covered hands"></div>
      <div class="photo-girl" role="img" aria-label="Photo of a smiling girl showing paint-covered hands"></div>

      <svg class="bands" viewBox="0 0 1620 775" aria-hidden="true">
        <polygon points="615,275 1110,290 1145,405 660,405 700,340" fill="var(--orange-deep)"/>
        <path d="M420 595 L1095 585 L1100 690 L410 698 L428 650 Z" fill="var(--red)"/>
      </svg>

      <div class="brand">
        <div class="brand-name"><span class="brand-dot"></span>mno Schools</div>
        <div class="brand-tagline">Daycare Kindergarten Primary</div>
      </div>

      <h1 class="headline">Bilingual D/E</h1>
      <h2 class="subheadline">Small Classes</h2>

      <p class="offer offer-daycare">Daycare</p>
      <p class="offer offer-kindergarten"><span class="accent">Private</span><span class="plain">Kindergarten</span></p>
      <p class="offer offer-school">Private School from <span class="year">2024</span></p>

      <div class="contact">
        <p class="contact-address">Lindenweg 12 8000 Musterdorf</p>
        <p class="contact-line">+41 79 555 01 23 | www.mno-daycare.ch</p>
      </div>
    </div>
  </div>
</body>
</html>
```